Technology solutions catalog

Were looking for a catalogue to supplement our website and corporate branding.

Our website will give you a good understanding of our products and services as well as our theme.

Our base colour and logo is red, white and grey.

www.voltrane.com.au

The aim of the catalogue is to showcase our business IT services & solutions. This will be a mix of education about the new solutions available to small and medium business today and how these solutions can increase productivity.

We would also like tip sections

This isn't all about selling but also about educating SMB's of the new and exciting IT solutions available today and having them book a free consult with us to discuss further about how we can help the business.

Solutions and area's that the catalogue will need to cover include

Front Cover -
-About us section, with our business contact information (1st page)
- Introduction. (2nd page)
-Communication Solutions - this includes Email, IP phones and business IT networks (2 pages)
- Data & Storage solutions (2 pages)
- Hardware (1 pages)
- Business IT health check list (1 page)
- Services and support offering (2 pages)
- Software & Popular cloud solutions (2 pages)
- Website / E-commerce solutions (2 pages)
Back cover

Based on two pages per solution the whole catalogue will be around 14 pages.

We don't need any text content done. We would like Headings on pages including page numbers. Footer please.

We're looking for a template that we can have our designer finish off by adding in some further product and service image and text.

Thank you for your consideration

Target Market(s)

IT for small and medium businesses

Industry/Entity Type

Supplement

Requirements
Must have
• Size A4
• Design supplied in Adobe indesign so we can edit and add our text and content
• Clean design

```html
<!DOCTYPE html>
<html lang="en">
<head>
<meta charset="utf-8">
<title>Voltrane Catalogue – About Us &amp; Our Mission</title>
<link rel="stylesheet" href="https://fonts.googleapis.com/css2?family=Montserrat:wght@300;400;600;700&display=swap">
<style>
  :root {
    --backdrop: #e2e2e2;
    --page-top: #f7fafb;
    --page-bottom: #e3eef1;
    --ink-dark: #555a5e;
    --ink-mid: #6d7377;
    --ink-light: #8d9397;
    --brand-red: #d8261f;
    --brand-red-soft: rgba(216, 38, 31, 0);
    --band-grey: #939393;
    --icon-cell: #cfd1d2;
    --panel-grey: #a4a4a4;
    --map-tone: #d3e0e5;
    --white: #ffffff;
  }
  * { box-sizing: border-box; margin: 0; padding: 0; }
  html, body {
    width: 1200px;
    height: 900px;
    overflow: hidden;
    background: var(--backdrop);
    font-family: "Montserrat", sans-serif;
  }
  .spread {
    position: absolute;
    left: 40px;
    top: 252px;
    width: 1120px;
    height: 396px;
    display: flex;
    box-shadow: 0 6px 18px rgba(0, 0, 0, 0.12);
  }
  .page {
    position: relative;
    width: 560px;
    height: 396px;
    background: linear-gradient(160deg, var(--page-top) 0%, var(--page-bottom) 100%);
    overflow: hidden;
  }
  .page--left::after {
    content: "";
    position: absolute;
    top: 0; right: 0;
    width: 26px; height: 100%;
    background: linear-gradient(90deg, rgba(0,0,0,0) 0%, rgba(0,0,0,0.07) 100%);
  }
  .page--right::before {
    content: "";
    position: absolute;
    top: 0; left: 0;
    width: 20px; height: 100%;
    background: linear-gradient(90deg, rgba(0,0,0,0.07) 0%, rgba(0,0,0,0) 100%);
  }

  /* Shared heading row: title followed by a fading red rule */
  .heading-row {
    position: absolute;
    display: flex;
    align-items: center;
    gap: 14px;
  }
  .heading-rule {
    flex: 1;
    height: 3px;
    margin-top: 4px;
    background: linear-gradient(90deg, var(--brand-red) 0%, var(--brand-red) 55%, var(--brand-red-soft) 100%);
  }

  /* Left page: About */
  .about-heading-row { left: 42px; top: 34px; width: 480px; }
  .about-heading {
    font-size: 15px;
    color: var(--ink-dark);
    white-space: nowrap;
  }
  .about-heading strong { font-weight: 700; }
  .about-heading .tagline { font-weight: 300; color: var(--ink-light); }
  .about-copy {
    position: absolute;
    left: 42px;
    top: 66px;
    width: 420px;
    font-size: 6.5px;
    line-height: 1.55;
    color: var(--ink-mid);
    font-weight: 600;
  }
  .about-copy p { margin-bottom: 6px; }
  .about-copy ul { list-style: none; margin-bottom: 6px; }
  .world-map {
    position: absolute;
    left: 42px;
    top: 196px;
    width: 220px;
    height: 96px;
    border-radius: 4px;
    background: linear-gradient(180deg, var(--map-tone) 0%, rgba(211, 224, 229, 0.35) 100%);
  }

  /* Right page: Mission */
  .mission-heading-row { left: 64px; top: 70px; width: 430px; }
  .mission-heading {
    font-size: 13px;
    font-weight: 700;
    color: var(--ink-dark);
    white-space: nowrap;
  }
  .mission-panel {
    position: absolute;
    left: 120px;
    top: 114px;
    width: 340px;
    height: 216px;
    background: var(--panel-grey);
  }
  .mission-list { list-style: none; }
  .mission-item {
    position: absolute;
    left: 70px;
    width: 390px;
    height: 44px;
    display: flex;
    background: var(--band-grey);
  }
  .mission-item:nth-child(1) { top: 114px; }
  .mission-item:nth-child(2) { top: 166px; }
  .mission-item:nth-child(3) { top: 218px; }
  .mission-item__icon {
    flex: 0 0 50px;
    height: 100%;
    background: var(--icon-cell);
    display: flex;
    align-items: center;
    justify-content: center;
  }
  .mission-item__body {
    padding: 7px 0 0 14px;
    color: var(--white);
  }
  .mission-item__title { font-size: 8.5px; font-weight: 700; margin-bottom: 2px; white-space: nowrap; }
  .mission-item__text { font-size: 6px; font-weight: 400; line-height: 1.4; width: 170px; opacity: 0.9; }
</style>
</head>
<body>
  <main class="spread">
    <section class="page page--left">
      <div class="heading-row about-heading-row">
        <h1 class="about-heading"><strong>About Voltrane</strong> <span class="tagline">| Just a bit about us</span></h1>
        <div class="heading-rule"></div>
      </div>
      <div class="about-copy">
        <p>Founded in 2009, Voltrane is an Australian information technology company helping small and medium businesses work smarter through simple and effective technology solutions.</p>
        <ul>
          <li>Industries we have supported include:</li>
          <li>Retail, Hospitality, Dental and Medical Practices</li>
          <li>Accounting, Legal, Trades and Logistics</li>
          <li>Professional Services</li>
          <li>Not-for-profits</li>
        </ul>
        <p>From the start we wanted to provide small and medium businesses with great service, leading information technology and clear, effective advice.</p>
      </div>
      <div class="world-map" role="img" aria-label="Faint world map"></div>
    </section>

    <section class="page page--right">
      <div class="heading-row mission-heading-row">
        <h2 class="mission-heading">Our Mission</h2>
        <div class="heading-rule"></div>
      </div>

      <div class="mission-panel"></div>

      <ul class="mission-list">
        <li class="mission-item">
          <div class="mission-item__icon">
            <svg width="34" height="16" viewBox="0 0 34 16" aria-hidden="true" fill="var(--brand-red)">
              <rect x="0" y="9" width="2" height="7"/><rect x="3" y="7" width="2" height="9"/>
              <rect x="6" y="10" width="2" height="6"/><rect x="9" y="6" width="2" height="10"/>
              <rect x="12" y="8" width="2" height="8"/><rect x="15" y="4" width="2" height="12"/>
              <rect x="18" y="7" width="2" height="9"/><rect x="21" y="2" width="2" height="14"/>
              <rect x="24" y="5" width="2" height="11"/><rect x="27" y="0" width="2" height="16"/>
              <rect x="30" y="4" width="2" height="12"/>
            </svg>
          </div>
          <div class="mission-item__body">
            <h3 class="mission-item__title">Grow Your Business</h3>
            <p class="mission-item__text">Leverage technology to grow your business with simple, effective and affordable solutions.</p>
          </div>
        </li>
        <li class="mission-item">
          <div class="mission-item__icon">
            <svg width="20" height="20" viewBox="0 0 20 20" aria-hidden="true">
              <circle cx="10" cy="10" r="9" fill="none" stroke="var(--brand-red)" stroke-width="1.5"/>
              <circle cx="10" cy="10" r="6" fill="var(--brand-red)"/>
            </svg>
          </div>
          <div class="mission-item__body">
            <h3 class="mission-item__title">We Manage your Technology</h3>
            <p class="mission-item__text">We manage all your technology so you can focus on your business and growing customers.</p>
          </div>
        </li>
        <li class="mission-item">
          <div class="mission-item__icon">
            <svg width="18" height="20" viewBox="0 0 18 20" aria-hidden="true">
              <path d="M9 1 L17 4 L17 10 C17 15 13 18 9 19 C5 18 1 15 1 10 L1 4 Z" fill="var(--brand-red)"/>
              <path d="M5 10 L8 13 L13 7" fill="none" stroke="#ffffff" stroke-width="1.6"/>
            </svg>
          </div>
          <div class="mission-item__body">
            <h3 class="mission-item__title">Protect</h3>
            <p class="mission-item__text">We secure and protect your technology to reduce your business risk.</p>
          </div>
        </li>
      </ul>
    </section>
  </main>
</body>
</html>
```